An internal sign in a physiotherapy clinic with gym. About working hard

We are a physiotherapy clinic / gym and we are wanting an internal wall to be a large sign with a great slogan
We are after 3 parts to it
1. The image / backdrop
2. The slogan
3. Our clinic logo

I have attached some images of the concept of what we are after. It can be climbing a mountain, rockclimbing and even hard work in a gym.

The slogan is:
"IF IT DOESN'T CHALLENGE YOU, IT WON'T CHANGE YOU"

Logo
I have attached a few different versions of our logo to assist you in the sign based on the background

THE SIGN SIZE WILL BE:
2935mm wide x 1885mm high

```html
<!DOCTYPE html>
<html lang="en">
<head>
<meta charset="utf-8">
<title>Kestrel Sports Medicine – Wall Sign</title>
<link rel="stylesheet" href="https://fonts.googleapis.com/css2?family=Orbitron:wght@500;700&display=swap">
<style>
  :root {
    --navy: #141a45;
    --sky: #45c0e6;
    --white: #ffffff;
    --page: #ffffff;
    --photo-dark: #3a3634;
    --photo-mid: #8a7f76;
    --photo-warm: #b0463e;
  }
  html, body {
    margin: 0;
    padding: 0;
    width: 1200px;
    height: 2561px;
    overflow: hidden;
    background: var(--page);
  }
  .sign {
    position: absolute;
    left: 194px;
    top: 1931px;
    width: 814px;
    height: 524px;
    overflow: hidden;
    font-family: "Orbitron", sans-serif;
    font-weight: 500;
  }
  .sign__photo {
    position: absolute;
    inset: 0;
    background:
      radial-gradient(ellipse 40% 30% at 30% 50%, rgba(150,100,80,0.55), transparent 70%),
      linear-gradient(180deg, var(--photo-dark) 0%, var(--photo-mid) 45%, #d9d6d2 70%, var(--photo-warm) 88%, #2c2a2a 100%);
  }
  .sign__panels {
    position: absolute;
    inset: 0;
    width: 814px;
    height: 524px;
  }
  .sign__name {
    position: absolute;
    left: 390px;
    right: 0;
    top: 70px;
    margin: 0;
    text-align: center;
    font-size: 58px;
    font-weight: 700;
    line-height: 1;
    letter-spacing: 1px;
    color: var(--white);
  }
  .sign__slogan {
    position: absolute;
    left: 390px;
    right: 0;
    top: 198px;
    margin: 0;
    text-align: center;
    font-size: 33px;
    font-weight: 500;
    line-height: 45px;
    color: var(--white);
  }
  .sign__slogan .accent { color: var(--sky); }
  .sign__clinic {
    position: absolute;
    left: 390px;
    right: 0;
    top: 424px;
    margin: 0;
    text-align: center;
    font-size: 27px;
    line-height: 30px;
    font-weight: 500;
    color: var(--navy);
    letter-spacing: 1px;
  }
</style>
</head>
<body>
  <main class="sign">
    <div class="sign__photo" role="img" aria-label="Photo of an athlete climbing a rope in a gym, with red medicine balls on a rack below"></div>

    <svg class="sign__panels" viewBox="0 0 814 524" preserveAspectRatio="none" aria-hidden="true">
      <path class="panel-stripe" fill="var(--sky)"
        d="M250,0 L814,0 L814,524 L395,524 L403,490 L400,418 C405,320 370,250 320,190 C265,125 240,70 250,0 Z"/>
      <path class="panel-main" fill="var(--navy)"
        d="M305,0 L814,0 L814,524 L395,524 L403,490 L415,418 C420,330 400,270 365,210 C320,140 295,70 305,0 Z"/>
      <path class="panel-band" fill="var(--sky)"
        d="M360,418 L814,418 L814,490 L360,490 A36,36 0 0 1 360,418 Z"/>
    </svg>

    <p class="sign__name">KESTREL</p>

    <p class="sign__slogan">
      If It <span class="accent">DOESN'T</span><br>
      CHALLENGE You,<br>
      It <span class="accent">WON'T</span><br>
      CHANGE You
    </p>

    <p class="sign__clinic">KESTREL<br>SPORTS MEDICINE</p>
  </main>
</body>
</html>
```